Plan of Joint Exploration Venture

I need a multi page prospects design. A cover page, table of contents, and content pages. I'm looking for the basic design now for each page, with content to be filled in later. For now, you can use blank content or random content pulled from anywhere. The table of contents will include: Investment Overview, Details of the Offer, Details of the Strategy, and Management Team Bios. Please use the logo and pictures attached; also, I've attached a general example.

```html
<!DOCTYPE html>
<html lang="en">
<head>
<meta charset="utf-8">
<title>Northvale Energy – Management Team Bios</title>
<link href="https://fonts.googleapis.com/css2?family=Arimo:wght@400;700&family=Open+Sans:wght@300;400&display=swap" rel="stylesheet">
<style>
  :root {
    --backdrop: #151515;
    --brand-red: #7d1a1e;
    --brand-red-bright: #b0232a;
    --page-white: #ffffff;
    --text-grey: #6b6b6b;
    --text-dark: #2b2b2b;
    --sand-light: #e9cfa4;
    --sand-dark: #b78a55;
  }
  * { margin: 0; padding: 0; box-sizing: border-box; }
  html, body { width: 1200px; height: 1000px; overflow: hidden; background: var(--backdrop); }
  .canvas { position: relative; width: 1200px; height: 1000px; }

  .page { position: absolute; overflow: hidden; background: var(--page-white); }
  .page--cover { left: 32px; top: 53px; width: 548px; height: 774px; }
  .page--bios { left: 611px; top: 192px; width: 544px; height: 769px; }

  .cover-photo {
    position: absolute; inset: 0;
    background: linear-gradient(180deg, #d9d2c9 0%, #e6d3b6 40%, var(--sand-light) 60%, var(--sand-dark) 100%);
  }
  .cover-swoosh { position: absolute; left: 0; top: 0; width: 548px; height: 80px; }
  .cover-title {
    position: absolute; left: 150px; top: 12px; width: 340px; text-align: center;
    font: 700 26px/1 "Arimo", Arial, sans-serif; color: var(--page-white);
  }
  .cover-web {
    position: absolute; left: 60px; top: 747px;
    font: 400 10px/1 "Open Sans", sans-serif; letter-spacing: 1.5px; color: #e9e2d8;
  }
  .page-number {
    position: absolute; width: 34px; height: 34px; border-radius: 50%;
    background: var(--brand-red); color: #f2d8d8;
    font: 400 8px/34px "Arimo", Arial, sans-serif; text-indent: 6px;
  }
  .page--cover .page-number { left: 530px; top: 726px; }
  .page--bios .page-number { left: 528px; top: 722px; }

  .bios-swoosh { position: absolute; left: 0; top: 0; width: 544px; height: 80px; }
  .brand-name {
    position: absolute; left: 28px; top: 72px; display: flex; align-items: center; gap: 8px;
    font: 400 26px/1 "Arimo", Arial, sans-serif; color: var(--brand-red);
  }
  .brand-name .brand-dot { width: 22px; height: 22px; border-radius: 50%; background: var(--brand-red); }

  .bios-heading {
    position: absolute; left: 54px; top: 151px;
    font: 700 18px/1 "Arimo", Arial, sans-serif; color: var(--brand-red-bright);
  }
  .bios-column {
    position: absolute; top: 178px;
    font: 300 10.4px/12.4px "Open Sans", sans-serif; color: var(--text-grey);
    text-align: justify;
  }
  .bios-column--left { left: 41px; width: 199px; }
  .bios-column--right { left: 285px; width: 236px; }
  .bios-column h3 {
    font: 700 10.4px/12.4px "Arimo", Arial, sans-serif; color: var(--text-dark); text-align: left;
  }
  .bios-column .spacer { height: 12px; }

  .world-map {
    position: absolute; left: 268px; top: 528px; width: 276px; height: 120px;
    background: radial-gradient(ellipse at center, #dcdcdc 0%, #eeeeee 55%, rgba(255,255,255,0) 80%);
  }
  .team-photo {
    position: absolute; left: 249px; top: 628px; width: 282px; height: 120px;
    background: linear-gradient(180deg, #cfd4da 0%, #5d6570 55%, #2e3238 100%);
    border-radius: 40px 40px 0 0;
  }
  .bios-web {
    position: absolute; left: 37px; top: 743px;
    font: 400 10px/1 "Open Sans", sans-serif; letter-spacing: 1.5px; color: var(--text-grey);
  }
</style>
</head>
<body>
<div class="canvas">

  <section class="page page--cover">
    <div class="cover-photo" role="img" aria-label="Photograph of oil pumpjacks in a sandy desert with a large pipeline in the foreground"></div>
    <svg class="cover-swoosh" viewBox="0 0 548 80" preserveAspectRatio="none" aria-hidden="true">
      <path d="M58 0 H548 V30 C470 75 330 82 220 56 C150 40 100 18 58 0 Z" fill="var(--brand-red)"/>
    </svg>
    <h1 class="cover-title">Management Team Bios</h1>
    <div class="cover-web">www.northvale.com</div>
    <div class="page-number">03</div>
  </section>

  <section class="page page--bios">
    <svg class="bios-swoosh" viewBox="0 0 544 80" preserveAspectRatio="none" aria-hidden="true">
      <path d="M54 0 H530 C500 40 420 78 310 78 C200 78 110 40 54 0 Z" fill="var(--brand-red)"/>
    </svg>
    <div class="brand-name"><span class="brand-dot"></span>Northvale Energy</div>

    <h2 class="bios-heading">Management Team Bios</h2>

    <div class="bios-column bios-column--left">
      <h3>7.1 Overview</h3>
      <p>The Board is composed of individuals with corporate governance experience finance, legal and corporate governance sectors. The Company's management is composed of individuals who have extensive experience in the global oil and gas industry.</p>
      <p>The Board and management's focus will be to create capital growth for Shareholders through the acquisition, assessment and exploitation of petroleum assets in an efficient and expeditious manner.</p>
      <div class="spacer"></div>
      <h3>7.2 Board of Directors</h3>
      <div class="spacer"></div>
      <p>Directors, including their experience, positions and independence.</p>
      <h3>Mr Daniel Marsh<br>(Non-Executive Chairman)</h3>
      <p>Daniel Marsh is a Eastbrook University law graduate, and is currently a practising solicitor with his own firm Hollis &amp; Marsh Lawyers.</p>
      <p>Daniel is a director on a number of private company boards and advisory boards. Daniel has a long history with the Regional Football League (RFL) and was the Riverton Football Club President from 1992 to 2002. In addition, Daniel was the former Commissioner of the RFL.</p>
    </div>

    <div class="bios-column bios-column--right">
      <h3>Jordan Hale (Director &amp; Chief<br>Executive Officer)</h3>
      <div class="spacer"></div>
      <p>Jordan is a Chartered Financial Analyst (CFA), a Chartered Accountant (ACA) and has completed degrees in Economics and Commerce at the Southgate University and has an extensive career in the Finance Industry.</p>
      <p>Jordan is a Consultant to the Oil &amp; Gas Industry. Jordan was previously an Oil &amp; Gas Analyst at Calder Securities responsible for coverage of small-mid capitalisation Oil &amp; Gas companies and has previously worked as an Energy Analyst at Ashford Partners covering large and mid-cap Energy companies and more recently, Marlow Stockbroking where he covered a basket of mid-capitalisation oil and gas companies. In addition to this Jordan has over 10 years' experience in the Institutional banking and finance sector where he has held positions at Eastline Institutional Bank, Norbridge Capital and Harbour Banking Group responsible for the origination and execution of transactions across the Energy &amp; Resources and Infrastructure client base.</p>
      <div class="spacer"></div>
      <p>Jordan is classified as a non-independent Director</p>
    </div>

    <div class="world-map" role="img" aria-label="Faint grey world map"></div>
    <div class="team-photo" role="img" aria-label="Photograph of a group of business people in suits standing together"></div>
    <div class="bios-web">www.northvale.com</div>
    <div class="page-number">03</div>
  </section>

</div>
</body>
</html>
```